Property Management Special Flyer - this month only deal

We need a flyer that's design aligns with the style of our website and regular price package attached.
We are a high quality service company that offers property management along Sydney's Northern Beaches.
This month we want to offer a deal where we are waiving Advertising Fees and a special management rate of 5% for this month (Aug) only.
Please show all the same details as on the "Tenancy and Upkeep Bundle" flyer but advertising the fact that this month only we are waiving the $350 advertising fee and a special Management fee of 5%.
I would like an A4 print ready version (with bleed if nec), an PDF version so we can email it to clients and an editable Photoshop PSD layered file so we can edit text if necessary for future use.
We would like to use the same background image as used in the price package flyer attached (background image also attached)
We want this flyer to capture attention but still look professional and clean like our website.

```html
<!DOCTYPE html>
<html lang="en">
<head>
<meta charset="utf-8">
<title>All Inclusive Package Flyer – August Special</title>
<link href="https://fonts.googleapis.com/css2?family=Barlow+Condensed:ital,wght@1,600&family=Source+Sans+3:wght@400;600&display=swap" rel="stylesheet">
<style>
  :root{
    --page-bg:#d9d9d9;
    --paper:#ffffff;
    --teal:#2aa3a8;
    --sky:#27b6e8;
    --deep-blue:#0f5c90;
    --mid-blue:#1b80bd;
    --frame:#b9cfdc;
    --ink:#454545;
    --muted:#6b6b6b;
    --panel:#e6e6e6;
    --footer:#343a42;
  }
  *{margin:0;padding:0;box-sizing:border-box}
  html,body{width:1200px;height:1200px;overflow:hidden;background:var(--page-bg)}
  body{position:relative;font-family:"Source Sans 3",Arial,sans-serif}
  .flyer{
    position:absolute;left:176px;top:0;width:900px;height:1273px;
    background:var(--paper);transform:scale(0.9425);transform-origin:0 0;overflow:hidden;
  }
  .hero{position:absolute;left:0;top:0;width:900px;height:700px}
  .hero-title{
    position:absolute;left:232px;top:478px;
    font-family:"Barlow Condensed","Arial Narrow",sans-serif;font-style:italic;font-weight:600;
    font-size:50px;letter-spacing:-0.5px;color:#111;
  }
  .includes{position:absolute;left:28px;top:644px}
  .includes-title{color:var(--teal);font-size:21px;font-weight:400;margin-bottom:10px}
  .includes-list{list-style:none;color:var(--ink);font-size:17.5px;line-height:26.3px}
  .includes-list li{position:relative;padding-left:16px;max-width:380px}
  .includes-list li::before{
    content:"";position:absolute;left:0;top:9px;width:9px;height:9px;border-radius:50%;
    background:var(--teal);
  }
  .includes-list li::after{
    content:"";position:absolute;left:2px;top:11.5px;width:3px;height:3px;
    border-top:1.2px solid #fff;border-right:1.2px solid #fff;transform:rotate(45deg);
  }
  .pricing{position:absolute;left:462px;top:753px;width:428px}
  .pricing-head{
    height:50px;background:var(--teal);color:#fff;font-size:18.5px;font-weight:400;
    padding-left:22px;line-height:52px;
  }
  .pricing-body{margin-top:11px;background:var(--panel);padding:17px 8px 20px 14px}
  .price-row{
    display:flex;height:26px;background:#fff;margin-bottom:8px;align-items:center;
    font-size:11.5px;color:var(--muted);
  }
  .price-row:last-child{margin-bottom:0}
  .price-label{width:223px;padding-left:5px;flex:none}
  .price-row.is-key{color:#333}
  .price-row.is-deal .price-value{color:var(--teal);font-weight:600}
  .price-note{font-size:7px;font-weight:400}
  .footer-stripe{position:absolute;left:0;top:1145px;width:900px;height:12px;background:var(--teal)}
  .footer{position:absolute;left:0;top:1157px;width:900px;height:116px;background:var(--footer);color:#fff}
  .brand{position:absolute;left:45px;top:41px;display:flex;align-items:center;gap:10px;
    font-size:26px;font-weight:600;letter-spacing:0.3px}
  .brand-mark{width:14px;height:14px;background:var(--teal)}
  .contact{position:absolute;left:507px;top:21px;font-size:14.5px;line-height:17px;font-style:normal}
</style>
</head>
<body>
<main class="flyer">
  <svg class="hero" viewBox="0 0 900 700">
    <defs>
      <linearGradient id="waveBlue" x1="0" y1="0" x2="0" y2="1">
        <stop offset="0" stop-color="#1b80bd"/>
        <stop offset="1" stop-color="#0b4f80"/>
      </linearGradient>
      <linearGradient id="streetScene" x1="0" y1="0" x2="0" y2="1">
        <stop offset="0" stop-color="#3aa6df"/>
        <stop offset="0.3" stop-color="#8fb6c4"/>
        <stop offset="0.6" stop-color="#5c7a48"/>
        <stop offset="0.85" stop-color="#8c8c88"/>
        <stop offset="1" stop-color="#6f6f6f"/>
      </linearGradient>
      <linearGradient id="promenadeScene" x1="0" y1="0" x2="0" y2="1">
        <stop offset="0" stop-color="#5ab0e2"/>
        <stop offset="1" stop-color="#2c4a66"/>
      </linearGradient>
      <linearGradient id="harbourScene" x1="0" y1="0" x2="0" y2="1">
        <stop offset="0" stop-color="#2a8fd6"/>
        <stop offset="0.5" stop-color="#6aa3b8"/>
        <stop offset="1" stop-color="#13609a"/>
      </linearGradient>
    </defs>
    <path class="wave-light" fill="var(--sky)" d="M0,0 H900 V520 C860,640 720,700 520,695 C380,690 290,665 200,630 V0 Z"/>
    <path class="wave-deep" fill="url(#waveBlue)" d="M0,0 H900 V455 C860,600 720,668 545,668 C420,668 320,648 225,622 V0 Z"/>
    <path class="street-photo" role="img" aria-label="Photo of modern terraced homes with gardens and stairs under a blue sky"
      fill="url(#streetScene)"
      d="M0,0 H790 C800,90 805,220 790,330 C770,460 700,555 560,565 H225 V487 H0 Z"/>
    <rect class="photo-frame" x="673" y="0" width="227" height="155" fill="var(--frame)"/>
    <rect role="img" aria-label="Photo of a waterfront promenade" x="692" y="12" width="191" height="128" fill="url(#promenadeScene)"/>
    <rect class="photo-frame" x="0" y="487" width="225" height="155" fill="var(--frame)"/>
    <rect role="img" aria-label="Photo of a harbour with moored boats" x="12" y="503" width="198" height="124" fill="url(#harbourScene)"/>
  </svg>
  <h1 class="hero-title">ALL INCLUSIVE PACKAGE</h1>

  <section class="includes">
    <h2 class="includes-title">INCLUDES:</h2>
    <ul class="includes-list">
      <li>Securing Tenant</li>
      <li>Reference/Database Checking</li>
      <li>Lease Preparation and Signing</li>
      <li>Direct Deposit rent collection</li>
      <li>Zero arrears policy management</li>
      <li>Payment of Rates and levies</li>
      <li>Insurance management</li>
      <li>Coordination or all repairs and maintenance</li>
      <li>Regular rent reviews and renewals</li>
      <li>Detailed ingoing, ongoing and outgoing inspections with photos and videos – viewable through your personal Landlord portal</li>
      <li>Bond management – lodging and refunding</li>
      <li>Electronic monthly and EOFY statements</li>
      <li>Annual scheduled maintenance report</li>
      <li>Regulation/compliance management</li>
      <li>Tribunal Representation</li>
    </ul>
  </section>

  <section class="pricing">
    <h2 class="pricing-head">All Inclusive Package</h2>
    <div class="pricing-body">
      <div class="price-row is-key is-deal"><span class="price-label">Management Rate:</span><span class="price-value">5% <span class="price-note">+ GST of rental income</span> – August only</span></div>
      <div class="price-row"><span class="price-label">Letting Fee:</span><span class="price-value">No Charge</span></div>
      <div class="price-row is-deal"><span class="price-label">Advertising:</span><span class="price-value">$350 fee waived – August only</span></div>
      <div class="price-row"><span class="price-label">Professional Photography:</span><span class="price-value">$199 <span class="price-note">(inc GST)</span> 4 x Photos</span></div>
      <div class="price-row"><span class="price-label">Statements:</span><span class="price-value">No Charge</span></div>
      <div class="price-row"><span class="price-label">Lease Preperation:</span><span class="price-value">No Charge</span></div>
      <div class="price-row"><span class="price-label">Renewal Fees:</span><span class="price-value">No Charge</span></div>
    </div>
  </section>

  <div class="footer-stripe"></div>
  <footer class="footer">
    <div class="brand"><span>HARBOURLINE REALTY</span><span class="brand-mark"></span></div>
    <address class="contact">
      Sam Carter 0400 000 111 &nbsp;|&nbsp; Nina Holt 0400 000 222<br>
      Suite 4, 12 Shore Parade, Seaview NSW 2000<br>
      info@harbourlinerealty.example<br>
      www.harbourlinerealty.example
    </address>
  </footer>
</main>
</body>
</html>
```